Webshop for furniture and lamps

We need a design for a web shop with APP that should have two options:
1-Webshop in general which should attract to private customer in general and
2-Website that is meant to attract big customers as hotels and restaurants who would have their own customerize login.

That's the idea behind the shop.

It should be diveded into 4 parts
vintage furniture
rattan set outdoor and indoor
lamps and
wooden wall decor

The name of the shop is brisa novelta!

Please kindly make me an offer.

Reason: Dear designers, so far there hasn't been a design that really matched. Look up German web sites like www.fernblick-art.de or www.holzkante17.de... Haven't been convinced by designs! Sorry folks. Please submit some new ones. Kind regards Ned

```html
<!DOCTYPE html>
<html lang="en">
<head>
<meta charset="utf-8">
<title>brisa novelta – furniture & lamps</title>
<link href="https://fonts.googleapis.com/css2?family=Open+Sans:wght@400;600;700;800&display=swap" rel="stylesheet">
<style>
:root{
  --orange:#ef8a1f;
  --ink:#3b3b3b;
  --muted:#8a8a8a;
  --line:#dadada;
  --page:#e9e9e9;
  --panel:#ffffff;
  --brown:#4a3d33;
  --brown-dark:#362c25;
  --shade:rgba(25,25,25,.55);
}
*{box-sizing:border-box;margin:0;padding:0}
html,body{width:1200px;height:2584px;overflow:hidden}
body{font-family:"Open Sans",Arial,sans-serif;background:var(--page);color:var(--ink);position:relative;font-size:12px}
.abs{position:absolute}
.topbar{left:0;top:0;width:1200px;height:24px;background:#2f2f2f;color:#bbb;font-size:9px;line-height:24px;padding:0 88px}
.topbar .links{position:absolute;right:88px;top:0;display:flex;gap:26px}
.header{left:0;top:24px;width:1200px;height:100px;background:var(--panel)}
.logo{position:absolute;left:88px;top:34px;display:flex;align-items:center;gap:10px;font-weight:800;font-size:24px;color:var(--ink);text-transform:uppercase;letter-spacing:.5px}
.logo .mark{width:26px;height:26px;background:var(--orange)}
.nav{position:absolute;left:430px;top:44px;display:flex;gap:26px;font-size:11px;font-weight:700;text-transform:uppercase}
.nav .active{color:var(--orange)}
.hero{left:88px;top:136px;width:1024px;height:300px;background:linear-gradient(120deg,#c9b79e,#a88a68 55%,#7c634a)}
.hero .title{position:absolute;right:60px;top:60px;color:#fff;font-size:46px;font-weight:700;letter-spacing:2px}
.panel{background:var(--panel);border:1px solid var(--line)}
.side-title{font-weight:800;font-size:14px;text-transform:uppercase;padding:16px 18px;border-bottom:1px solid var(--line)}
.cat-list{list-style:none;padding:8px 18px;font-size:11px;color:var(--muted)}
.cat-list li{padding:9px 0;border-bottom:1px solid #eee}
.sec-title{font-weight:800;font-size:14px;text-transform:uppercase}
.promo-tag{position:absolute;left:16px;top:16px;background:var(--orange);color:#fff;font-weight:800;font-size:13px;padding:8px 16px;text-transform:uppercase}
.photo{border-radius:4px}
.name{font-size:9px;font-weight:700;text-transform:uppercase;text-align:center;margin-top:10px}
.price{color:var(--orange);font-weight:800;font-size:14px;text-align:center;margin-top:4px}
.buy{display:flex;justify-content:center;gap:6px;margin-top:8px}
.buy span{height:24px;border:1px solid var(--line);font-size:10px;line-height:22px;padding:0 10px}
.buy .cart{width:28px;background:var(--brown);border-color:var(--brown)}
.product{position:absolute;width:190px}
.product .photo{height:130px;margin:0 auto;width:160px}
.badge{position:absolute;left:0;top:-8px;background:#777;color:#fff;font-size:9px;font-weight:700;padding:3px 8px;z-index:1}
.badge.sale{background:var(--orange)}
.filter{position:absolute;right:18px;top:18px;font-size:9px;color:var(--muted)}
.view-all{left:460px;top:1648px;width:652px;height:36px;background:var(--brown);color:#fff;font-weight:700;font-size:11px;text-align:center;line-height:36px;text-transform:uppercase}
.banner{left:460px;top:1716px;width:652px;height:132px;background:linear-gradient(90deg,#c9a57a,#a98257 55%,#6f5137)}
.banner .txt{position:absolute;right:40px;top:40px;color:#fff;font-size:22px;font-weight:700}
.banner .txt small{display:block;font-size:10px;font-weight:400;color:#f3e3cc}
.blog p{font-size:10px;color:var(--muted);line-height:15px}
.blog h4{font-size:10px;font-weight:700;text-transform:uppercase;margin:14px 0 6px}
.tweet{display:flex;gap:12px;margin-bottom:22px}
.tweet .ico{width:30px;height:30px;border-radius:50%;background:var(--orange);flex:none}
.tweet p{font-size:9px;color:var(--muted);line-height:14px}
.tweet p b{color:var(--orange)}
.footer{left:0;top:2312px;width:1200px;height:272px;background:var(--brown-dark);color:#d7cbbf}
.fcol{position:absolute;top:28px;font-size:10px;line-height:20px}
.fcol h5{font-size:11px;font-weight:800;text-transform:uppercase;color:#fff;margin-bottom:8px}
.subscribe{display:flex;margin-top:14px}
.subscribe span{height:26px;background:#fff;width:170px}
.subscribe b{height:26px;background:var(--orange);color:#fff;font-size:10px;padding:0 12px;line-height:26px}
.social{display:flex;gap:8px;margin-top:4px}
.social i{width:20px;height:20px;border-radius:50%;background:#7b6a5c;display:block}
.pay{display:flex;gap:8px;margin-top:4px}
.pay i{width:26px;height:18px;background:#7b6a5c;display:block}
.fbottom{position:absolute;left:0;bottom:0;width:1200px;height:40px;border-top:1px solid #55473c;font-size:9px;line-height:40px;padding:0 88px;color:#a99a8c}
.fbottom .links{position:absolute;right:88px;top:0;display:flex;gap:24px}
.shade{left:0;top:0;width:1200px;height:2584px;background:var(--shade)}
.modal{left:268px;top:140px;width:680px;height:348px;background:var(--orange);color:#fff;text-align:center;padding-top:26px}
.modal h2{font-size:34px;font-weight:800;letter-spacing:1px}
.modal .emblem{width:42px;height:42px;border-radius:50%;background:#fff;margin:20px auto 18px;display:flex;align-items:center;justify-content:center}
.modal p{font-size:13px;line-height:20px}
.modal p b{font-weight:800}
.modal .site{margin-top:30px;font-size:11px}
</style>
</head>
<body>

<div class="abs topbar">Free delivery on all orders above 100 €
  <div class="links"><span>Wishlist</span><span>My Account</span><span>View Cart</span></div>
</div>

<header class="abs header">
  <div class="logo"><span class="mark"></span>brisa novelta</div>
  <nav class="nav"><span class="active">Home</span><span>Categories</span><span>About Us</span><span>FAQ</span><span>Contact Us</span></nav>
</header>

<div class="abs hero" role="img" aria-label="Slider photo of a furnished living room">
  <div class="title">SOLENA</div>
</div>

<aside class="abs panel" style="left:88px;top:464px;width:332px;height:356px">
  <div class="side-title">Shop by Category</div>
  <ul class="cat-list">
    <li>Vintage furniture</li>
    <li>Rattan sets outdoor and indoor</li>
    <li>Lamps</li>
    <li>Wooden wall decor</li>
  </ul>
</aside>

<section class="abs panel" style="left:460px;top:464px;width:652px;height:356px">
  <div class="promo-tag">Promo of the Month</div>
  <div class="abs" style="left:36px;top:90px;width:220px">
    <div class="name" style="text-align:left">Rattan Lounge Set 3 Pcs</div>
    <div class="price" style="text-align:left">€369.00</div>
    <div class="buy" style="justify-content:flex-start"><span>Add to cart</span><span class="cart"></span></div>
  </div>
  <div class="abs photo" style="left:300px;top:60px;width:250px;height:230px;background:linear-gradient(160deg,#6e4a30,#4b3020)" role="img" aria-label="Vintage wooden cabinet with open door"></div>
</section>

<aside class="abs panel" style="left:88px;top:868px;width:332px;height:492px">
  <div class="side-title">Best Seller</div>
  <div class="abs photo" style="left:96px;top:80px;width:140px;height:90px;background:linear-gradient(#b88a5e,#7c5636)" role="img" aria-label="Round rattan sofa set"></div>
  <div class="abs" style="left:0;top:176px;width:332px"><div class="name">Rattan Round Set</div><div class="price">€289.00</div><div class="buy"><span>Add to cart</span><span class="cart"></span></div></div>
  <div class="abs photo" style="left:96px;top:290px;width:140px;height:90px;background:linear-gradient(#c49a6c,#8a6040)" role="img" aria-label="Rattan outdoor seating"></div>
  <div class="abs" style="left:0;top:386px;width:332px"><div class="name">Rattan Garden Set</div><div class="price">€269.00</div><div class="buy"><span>Add to cart</span><span class="cart"></span></div></div>
</aside>

<section class="abs panel" style="left:460px;top:868px;width:652px;height:372px">
  <div class="abs sec-title" style="left:18px;top:18px">New Product</div>
  <div class="filter">Sort by: Newest &nbsp;|&nbsp; Price &nbsp;|&nbsp; Name</div>
  <div class="product" style="left:20px;top:84px"><span class="badge">NEW</span>
    <div class="photo" style="background:linear-gradient(#a5523a,#5e7a52 50%,#8c3f30)" role="img" aria-label="Painted vintage chest of drawers"></div>
    <div class="name">Vintage Painted Chest</div><div class="price">€329.00</div><div class="buy"><span>Add to cart</span><span class="cart"></span></div></div>
  <div class="product" style="left:231px;top:84px"><span class="badge sale">SALE</span>
    <div class="photo" style="background:linear-gradient(#7c4a35,#b0763e 50%,#5b3b28)" role="img" aria-label="Carved wooden sideboard"></div>
    <div class="name">Carved Wood Sideboard</div><div class="price">€419.00</div><div class="buy"><span>Add to cart</span><span class="cart"></span></div></div>
  <div class="product" style="left:442px;top:84px"><span class="badge">NEW</span>
    <div class="photo" style="background:linear-gradient(#5a5550,#3d3a37)" role="img" aria-label="Dark rattan bistro set"></div>
    <div class="name">Rattan Bistro Set</div><div class="price">€249.00</div><div class="buy"><span>Add to cart</span><span class="cart"></span></div></div>
</section>

<aside class="abs panel" style="left:88px;top:1400px;width:332px;height:320px">
  <div class="side-title">Special Offer</div>
  <div class="abs photo" style="left:126px;top:66px;width:80px;height:150px;background:linear-gradient(#6f4d34,#93633f 50%,#5a3c29)" role="img" aria-label="Tall vintage wooden cabinet"></div>
  <div class="abs" style="left:0;top:222px;width:332px"><div class="name">Vintage Tall Cabinet</div><div class="price">€399.00</div><div class="buy"><span>Add to cart</span><span class="cart"></span></div></div>
</aside>

<section class="abs panel" style="left:460px;top:1272px;width:652px;height:376px">
  <div class="abs sec-title" style="left:18px;top:18px">Featured Products</div>
  <div class="filter">Sort by: Popular &nbsp;|&nbsp; Price &nbsp;|&nbsp; Name</div>
  <div class="product" style="left:20px;top:84px"><span class="badge sale">SALE</span>
    <div class="photo" style="background:linear-gradient(#c4996a,#7d5434)" role="img" aria-label="Rattan dining set"></div>
    <div class="name">Rattan Dining Set</div><div class="price">€459.00</div><div class="buy"><span>Add to cart</span><span class="cart"></span></div></div>
  <div class="product" style="left:231px;top:84px">
    <div class="photo" style="background:linear-gradient(#9a7458,#5a3d2b)" role="img" aria-label="Solid wood dining table"></div>
    <div class="name">Solid Wood Table</div><div class="price">€279.00</div><div class="buy"><span>Add to cart</span><span class="cart"></span></div></div>
  <div class="product" style="left:442px;top:84px">
    <div class="photo" style="background:linear-gradient(#d8b374,#b89668 50%,#8a6a46)" role="img" aria-label="Floor lamp with woven shade"></div>
    <div class="name">Woven Floor Lamp</div><div class="price">€129.00</div><div class="buy"><span>Add to cart</span><span class="cart"></span></div></div>
</section>
<div class="abs view-all">View all items</div>

<div class="abs banner" role="img" aria-label="Photo of a rattan outdoor lounge on a terrace">
  <div class="txt">outside furniture<small>Rattan sets for terrace and garden</small></div>
</div>

<section class="abs panel blog" style="left:88px;top:1880px;width:332px;height:360px;padding:0 18px">
  <div class="side-title" style="padding-left:0">Latest from Blog</div>
  <h4>How to style rattan indoors</h4>
  <p>Light rattan pieces bring warmth to any room. Combine them with soft textiles and natural wood for a calm look.</p>
  <h4>Caring for vintage wood</h4>
  <p>Old wood needs gentle oil and a dry place. A few simple steps keep your favourite chest looking great.</p>
</section>

<section class="abs" style="left:440px;top:1880px;width:320px;height:360px">
  <div class="sec-title" style="padding:16px 0">Tweets</div>
  <div class="tweet"><span class="ico"></span><p><b>@brisanovelta</b> New rattan lounge sets just arrived in store, ready for summer.<br>2 hours ago</p></div>
  <div class="tweet"><span class="ico"></span><p><b>@brisanovelta</b> Our wooden wall decor collection is now twenty percent off.<br>1 day ago</p></div>
  <div class="tweet"><span class="ico"></span><p><b>@brisanovelta</b> Hotel and restaurant partners can now order with their own login.<br>3 days ago</p></div>
</section>

<section class="abs" style="left:780px;top:1880px;width:332px;height:360px">
  <div class="sec-title" style="padding:16px 0">Watch Our Video</div>
  <div class="abs" style="left:0;top:56px;width:332px;height:210px;background:linear-gradient(135deg,#8c7866,#4f4035)" role="img" aria-label="Video still of a furnished interior">
    <svg class="abs" style="left:136px;top:75px" width="60" height="60" viewBox="0 0 60 60"><circle cx="30" cy="30" r="28" fill="#fff" fill-opacity=".85"/><path d="M24 18 L42 30 L24 42 Z" fill="#4a3d33"/></svg>
  </div>
</section>

<footer class="abs footer">
  <div class="fcol" style="left:88px"><h5>Company</h5>About us<br>Our stores<br>Careers<br>Press<br>Contact</div>
  <div class="fcol" style="left:260px"><h5>Shipping</h5>Delivery info<br>Returns<br>Order tracking<br>Business orders<br>Payment</div>
  <div class="fcol" style="left:440px"><h5>FAQ</h5>Customer service<br>Privacy policy<br>Terms of sale<br>Gift cards<br>Site map</div>
  <div class="fcol" style="left:620px;width:280px"><h5>News &amp; Update</h5>Sign up to get our latest offers and news.
    <div class="subscribe"><span></span><b>SIGN UP</b></div></div>
  <div class="fcol" style="left:960px"><h5>Follow Us On</h5>
    <div class="social"><i></i><i></i><i></i><i></i><i></i></div>
    <h5 style="margin-top:18px">Payment Method</h5>
    <div class="pay"><i></i><i></i><i></i><i></i></div></div>
  <div class="fbottom">© 2015 brisa novelta. All rights reserved.
    <div class="links"><span>About us</span><span>Privacy policy</span><span>Terms</span><span>Contact</span><span>Site map</span></div></div>
</footer>

<div class="abs shade"></div>
<div class="abs modal">
  <h2>WELCOME VISITORS</h2>
  <div class="emblem">
    <svg width="22" height="22" viewBox="0 0 22 22"><circle cx="11" cy="7" r="4" fill="#ef8a1f"/><path d="M3 20 Q11 9 19 20 Z" fill="#ef8a1f"/></svg>
  </div>
  <p>Join us and get special promo every week<br>for New Member, please <b>SIGN UP</b> here.</p>
  <p style="margin-top:16px">Discount Membership <b>20% OFF</b> Now and Private Customer Membership <b>20% OFF</b> here.</p>
  <p class="site">www.brisanovelta.com</p>
</div>
<svg class="abs" style="left:920px;top:112px" width="28" height="28" viewBox="0 0 28 28"><circle cx="14" cy="14" r="12" fill="#fff" stroke="#555" stroke-width="2"/><path d="M10 10 L18 18 M18 10 L10 18" stroke="#555" stroke-width="2"/></svg>

</body>
</html>
```